Spanish Student Needs a Cover for his PhD Dissertation

Hi everyone :) So, I'm a Corneal surgeon currently finishing my PhD, with a dissertation focused on the evaluation of quality of life in patients affected by a disease called Keratoconus. Just so you know, Keratoconus is a condition in which the cornea (the frontal part of the way) gets thin and bulgy and it decreases vision. What I did during my PhD was designing a questionnaire for evaluating quality of life in this kind of patients.
I need to design a hard cover for my dissertation, which is 200 sheets long. I like kind of minimalistic and geometric designs but I am totally open to suggestions. What needs to be in the cover is the name of the dissertation "Diseño, desarrollo y validación de una encuesta para evaluar el compromiso visual y emocional subjetivos en pacientes con Queratocono" and my name, "Iñigo Tarrasco". The other thing that needs to go there is the logo of my university (Universidad de Montebrisa). Aside from that, anything else is up to the designer. It would be important to use the kind of "red" color I am using in the dissertation. I am attaching the frontal page of my dissertation so you know what kind of design and colors I am using.
In the back part, of the cover, there should be this small inscription: "Iñigo Tarrasco, MD, es un Oftalmólogo Subespecialista en Cirugía Refractiva de la Universidad Serrana Metropolitana (Colombia) y la Universidad de Montebrisa (España). Actualmente se desempeña como miembro del Departamento de Córnea y Cirugía Refractiva de la Clínica de Oftalmología Vallealto y como director de su propia compañía de emprendimiento médico Silver Heron Surgical". Please leave a space to place my picture; I will have it taken this week so I don't have it right now, you can just leave the blank spot and I will include it later
The size of the pages is standard "letter" size.
Thanks a lot!

Target Market(s)

PhD Scholars

Font styles to use
Serif

Requirements
Must have
• The "red" color I use on my font. It must be formal but "young".
Nice to have
• I like to keep the design clean, kind of "formal with a young" touch so to speak. I really like gray colors, so it would be nice to have broad areas of gray. I love geometrical designs.
I have uploaded a very early version a friend of mine made (it even had a different title); this can be a starting point for you to work on, but I am more than open to suggestions and new ideas.
Should not have
• Please don't use my whole name, Iñigo Tarrasco is fine. I don't like ALL CAPITALS.

```html
<!DOCTYPE html>
<html lang="es">
<head>
<meta charset="utf-8">
<title>Queratocono — Iñigo Tarrasco</title>
<link rel="stylesheet" href="https://fonts.googleapis.com/css2?family=Jost:wght@500;600;700&display=swap">
<style>
  :root {
    --paper: #ebe7e7;
    --ink: #0a0a0a;
    --rose: #e06262;
    --title-red: #c24a56;
    --deep-red: #a3272a;
    --rule: #d65a63;
  }
  html, body {
    margin: 0;
    padding: 0;
    overflow: hidden;
  }
  .cover {
    position: relative;
    width: 927px;
    height: 1200px;
    background: var(--paper);
    overflow: hidden;
    font-family: "Jost", "Futura", sans-serif;
    color: var(--ink);
  }
  .side-column {
    position: absolute;
    left: 757px;
    top: 0;
    width: 170px;
    height: 1200px;
    background: linear-gradient(180deg, var(--rose) 0%, var(--rose) 45%, var(--deep-red) 70%, var(--deep-red) 100%);
  }
  .university {
    position: absolute;
    left: 19px;
    top: 8px;
    width: 162px;
    height: 162px;
    display: flex;
    flex-direction: column;
    align-items: center;
    justify-content: center;
    gap: 10px;
    text-align: center;
  }
  .university-dot {
    width: 44px;
    height: 44px;
    border-radius: 50%;
    background: var(--ink);
  }
  .university-name {
    font-weight: 600;
    font-size: 15px;
    line-height: 1.2;
    color: var(--ink);
  }
  .header-rule {
    position: absolute;
    left: 0;
    top: 204px;
    width: 757px;
    height: 4px;
    background: var(--rule);
  }
  .title {
    position: absolute;
    left: 23px;
    top: 232px;
    margin: 0;
    font-weight: 700;
    font-size: 38px;
    line-height: 52px;
    letter-spacing: 0.2px;
    white-space: nowrap;
  }
  .title span { display: block; }
  .title .keyword {
    color: var(--title-red);
    font-size: 77px;
    line-height: 82px;
    margin-top: 2px;
    letter-spacing: 0.5px;
  }
  .photo-band {
    position: absolute;
    left: 0;
    top: 545px;
    width: 757px;
    height: 290px;
    background: radial-gradient(ellipse at 55% 45%, #d8d8d8 0%, #a9a9a9 45%, #6e6e6e 100%);
  }
  .photo-band-tint {
    position: absolute;
    left: 757px;
    top: 545px;
    width: 170px;
    height: 290px;
    background: linear-gradient(90deg, #6e2028 0%, #b8404a 55%, #c5565d 100%);
  }
  .author {
    position: absolute;
    right: 187px;
    top: 1012px;
    margin: 0;
    text-align: right;
    font-weight: 700;
    font-size: 63px;
    line-height: 104px;
    white-space: nowrap;
  }
  .author span { display: block; }
  .corner-mark {
    position: absolute;
    left: 0;
    bottom: 0;
  }
</style>
</head>
<body>
  <main class="cover">
    <div class="side-column"></div>

    <div class="university">
      <div class="university-dot"></div>
      <div class="university-name">Universidad de Montebrisa</div>
    </div>

    <div class="header-rule"></div>

    <h1 class="title">
      <span>Diseño, desarrollo y validación</span>
      <span>de una encuesta para evaluar</span>
      <span>el compromiso visual y emocional</span>
      <span>subjetivos en pacientes con</span>
      <span class="keyword">Queratocono</span>
    </h1>

    <div class="photo-band" role="img" aria-label="Fotografía en blanco y negro de un ojo con queratocono visto de perfil, mostrando la córnea abombada"></div>
    <div class="photo-band-tint" role="img" aria-label="Continuación de la fotografía del ojo con pestañas, teñida de rojo"></div>

    <p class="author">
      <span>Iñigo</span>
      <span>Tarrasco</span>
    </p>

    <svg class="corner-mark" width="56" height="56" viewBox="0 0 56 56" aria-hidden="true">
      <polygon points="0,0 0,56 56,56" fill="var(--deep-red)"/>
    </svg>
  </main>
</body>
</html>
```